Scrap Metal Recycling

We are looking for a simple yet bold business card. We already have the logo, please see attached. Color scheme of blue, black and white or just blue and white.

```html
<!DOCTYPE html>
<html lang="en">
<head>
<meta charset="utf-8">
<title>R.K. Alloys Inc. – Business Card</title>
<link href="https://fonts.googleapis.com/css2?family=Montserrat:wght@400;500;600;700&display=swap" rel="stylesheet">
<style>
  :root {
    --page-bg: #e4e6e6;
    --brand-blue-dark: #1f8bab;
    --brand-blue-light: #27a3c6;
    --brand-blue-text: #1f8fb5;
    --ink: #2a2b2d;
    --white: #ffffff;
    --card-shadow: 0 2px 5px rgba(0, 0, 0, 0.22);
  }
  * { box-sizing: border-box; margin: 0; padding: 0; }
  html, body {
    width: 1200px;
    height: 800px;
    overflow: hidden;
    background: var(--page-bg);
    font-family: "Montserrat", sans-serif;
  }
  .canvas {
    position: relative;
    width: 1200px;
    height: 800px;
  }
  .card {
    position: absolute;
    width: 440px;
    height: 272px;
    box-shadow: var(--card-shadow);
    overflow: hidden;
  }

  /* Front side */
  .card--front {
    left: 193px;
    top: 101px;
    background: linear-gradient(165deg, var(--brand-blue-dark) 0%, var(--brand-blue-dark) 35%, var(--brand-blue-light) 60%, var(--brand-blue-light) 100%);
    color: var(--white);
  }
  .front-brand {
    position: absolute;
    right: 38px;
    top: 40px;
    text-align: left;
  }
  .front-brand__name {
    font-size: 12.5px;
    font-weight: 600;
    letter-spacing: 0.2px;
    line-height: 1;
  }
  .front-brand__tagline {
    margin-top: 4px;
    font-size: 5.6px;
    font-weight: 500;
    letter-spacing: 1.9px;
  }
  .name-plate {
    position: absolute;
    left: -2px;
    top: 124px;
    width: 260px;
    height: 61px;
    border: 1px solid rgba(255, 255, 255, 0.9);
    border-left: none;
    border-radius: 0 8px 8px 0;
    padding: 10px 0 0 28px;
  }
  .name-plate__name {
    font-size: 22.5px;
    font-weight: 700;
    letter-spacing: 0.4px;
    line-height: 1.05;
  }
  .name-plate__role {
    font-size: 12px;
    font-weight: 500;
    letter-spacing: 0.3px;
    margin-top: 1px;
  }
  .contact-row {
    position: absolute;
    left: 27px;
    top: 204px;
    display: flex;
    font-size: 9.2px;
    font-weight: 400;
  }
  .contact-row__item {
    display: flex;
    align-items: center;
    gap: 7px;
  }
  .contact-row__item--address { width: 136px; }
  .contact-row__item--phone { width: 100px; }
  .contact-row__icon { width: 8px; height: 9px; fill: var(--white); flex: none; }

  /* Back side */
  .card--back {
    left: 567px;
    top: 424px;
    background: var(--white);
    text-align: center;
  }
  .back-brand {
    position: absolute;
    left: 0;
    right: 0;
    top: 112px;
  }
  .back-brand__name {
    font-size: 30px;
    font-weight: 600;
    color: var(--ink);
    line-height: 1;
    letter-spacing: 0.3px;
  }
  .back-brand__tagline {
    margin-top: 8px;
    font-size: 12.5px;
    font-weight: 500;
    letter-spacing: 4.6px;
    color: var(--brand-blue-text);
  }
  .back-website {
    position: absolute;
    left: 0;
    right: 0;
    top: 224px;
    font-size: 8.6px;
    font-weight: 500;
    color: var(--brand-blue-text);
  }
</style>
</head>
<body>
<main class="canvas">

  <section class="card card--front" aria-label="Business card front">
    <div class="front-brand">
      <div class="front-brand__name">R.K. ALLOYS INC.</div>
      <div class="front-brand__tagline">SCRAP METAL RECYCLING</div>
    </div>

    <div class="name-plate">
      <div class="name-plate__name">NAME SURNAME</div>
      <div class="name-plate__role">Job Position</div>
    </div>

    <div class="contact-row">
      <div class="contact-row__item contact-row__item--address">
        <svg class="contact-row__icon" viewBox="0 0 10 14" aria-hidden="true">
          <path d="M5 0C2.2 0 0 2.2 0 5c0 3.6 5 9 5 9s5-5.4 5-9c0-2.8-2.2-5-5-5zm0 7a2 2 0 1 1 0-4 2 2 0 0 1 0 4z"/>
        </svg>
        <span>Company address line</span>
      </div>
      <div class="contact-row__item contact-row__item--phone">
        <svg class="contact-row__icon" viewBox="0 0 14 14" aria-hidden="true">
          <path d="M3 0.5l2.2 2.8-1.3 1.6c.8 1.9 2.3 3.4 4.2 4.2l1.6-1.3L12.5 10l-1.5 2.6C5.5 12.8 0.9 8.2 0.9 2.5z"/>
        </svg>
        <span>+12 345 678 90</span>
      </div>
      <div class="contact-row__item contact-row__item--email">
        <svg class="contact-row__icon" viewBox="0 0 14 10" aria-hidden="true" style="width:9px;height:7px">
          <path d="M0 0h14v10H0z M1 1l6 4.5L13 1" fill="var(--white)"/>
          <path d="M0.8 0.8L7 5.3l6.2-4.5" fill="none" stroke="#2399bb" stroke-width="1"/>
        </svg>
        <span>email@yourcompany.com</span>
      </div>
    </div>
  </section>

  <section class="card card--back" aria-label="Business card back">
    <div class="back-brand">
      <div class="back-brand__name">R.K. ALLOYS INC.</div>
      <div class="back-brand__tagline">SCRAP METAL RECYCLING</div>
    </div>
    <div class="back-website">www.yourwebsite.com</div>
  </section>

</main>
</body>
</html>
```